Letterhead Design

I would like 2 different letterheads. One with each logo I have attached. Business info:
Larkfield Medical Billing, LLC
3870 N Cedar
Ossing, KS 66492
(866) 555-0143

```html
<!DOCTYPE html>
<html lang="en">
<head>
<meta charset="utf-8">
<title>Larkfield Medical Billing, LLC — Letterhead</title>
<link rel="stylesheet" href="https://fonts.googleapis.com/css2?family=Lato:wght@300;700&display=swap">
<style>
  :root {
    --page: #ffffff;
    --teal: #46e4c6;
    --slate: #2f4248;
    --ink-light: #ffffff;
  }
  html, body {
    margin: 0;
    padding: 0;
    overflow: hidden;
    background: var(--page);
  }
  .letterhead {
    position: relative;
    width: 849px;
    height: 1200px;
    background: var(--page);
    overflow: hidden;
    font-family: "Lato", sans-serif;
  }
  .brand {
    position: absolute;
    top: 38px;
    left: 40px;
    width: 80px;
    display: flex;
    flex-direction: column;
    align-items: center;
    gap: 6px;
  }
  .brand-mark {
    width: 40px;
    height: 40px;
    background: var(--slate);
  }
  .brand-name {
    margin: 0;
    font-weight: 700;
    font-size: 10px;
    line-height: 1.2;
    text-align: center;
    color: var(--slate);
  }
  .footer-wave {
    position: absolute;
    left: 0;
    top: 0;
    width: 849px;
    height: 1200px;
  }
  .footer-wave path {
    fill: var(--teal);
  }
  .contact {
    position: absolute;
    right: 9px;
    bottom: 18px;
    margin: 0;
    font-style: normal;
    font-weight: 300;
    font-size: 14px;
    line-height: 16.5px;
    text-align: right;
    color: var(--ink-light);
  }
</style>
</head>
<body>
  <main class="letterhead">
    <header class="brand">
      <span class="brand-mark" aria-hidden="true"></span>
      <p class="brand-name">Larkfield Medical Billing, LLC</p>
    </header>

    <svg class="footer-wave" viewBox="0 0 849 1200" aria-hidden="true">
      <path d="M38 1200 C 430 1190, 790 1060, 849 770 L 849 1200 Z"/>
    </svg>

    <address class="contact">
      Larkfield Medical Billing, LLC<br>
      3870 N Cedar<br>
      Ossing, KS 66492<br>
      (866) 555-0143
    </address>
  </main>
</body>
</html>
```